Varga Lillas Physiotherapy Business Card Vienna

We need a business card design for a newly created Physiotherapy company based in Vienna Austria.
We seek a simple, modern, minimalist design without too much color variation. The font should look young/fresh, but definitely not childish or so. Since we are a starting Business, we currently haven't got a logo, if you feel like a logo would fit your design, feel free to use one, but it's not necessary.
Target Market(s)
Healthcare, young and elderly people with mobility issues
Industry/Entity Type
Health And Wellness
Contact Information for Business Card
Name: Lilla Varga
Title description: Physiotherapist
Phone num: +43 664 5290 4816
e-mail: lilla.praxis@brelomail.com
Colors
Designer to choose colors to be used in the design.
Requirements
Must have
- Final design language must be in German, basically, the Title Description needs to be "Physiotherapeutin" the other details remain as in the English Language.
Nice to have
- Simple, modern, minimalist design
Should not have
- too many colors, Obvious use of a skeleton, skull, spline

```html
<!DOCTYPE html>
<html lang="de">
<head>
<meta charset="utf-8">
<title>Lilla Varga – Physiotherapie Visitenkarte</title>
<link rel="stylesheet" href="https://fonts.googleapis.com/css2?family=Noto+Sans:wght@400&display=swap">
<style>
  :root {
    --page-bg: #ffffff;
    --card-bg: #414141;
    --accent: #00bff2;
    --accent-deep: #135d8c;
    --text-dark: #0a0a0a;
    --text-light: #ffffff;
    --shade: rgba(0, 0, 0, 0.55);
  }
  * { box-sizing: border-box; margin: 0; padding: 0; }
  html, body {
    width: 1200px;
    height: 1200px;
    overflow: hidden;
    background: var(--page-bg);
    font-family: "Noto Sans", Tahoma, sans-serif;
  }
  .card {
    position: absolute;
    left: 51px;
    top: 260px;
    width: 1075px;
    height: 538px;
    background: var(--card-bg);
    overflow: hidden;
  }
  .card__band {
    position: absolute;
    left: 480px;
    top: 130px;
    width: 321px;
    height: 112px;
    background: linear-gradient(90deg, #0a8fb6 0%, var(--accent) 30%, var(--accent) 100%);
  }
  .card__panel-wrap {
    position: absolute;
    left: 22px;
    top: 22px;
    width: 567px;
    height: 498px;
    filter: drop-shadow(14px 6px 18px var(--shade));
  }
  .card__panel {
    position: absolute;
    inset: 0;
    background: var(--accent);
    clip-path: polygon(0 0, 100% 0, 65.3% 100%, 0 100%);
  }
  .card__title {
    position: absolute;
    left: 47px;
    top: 18px;
    font-size: 54px;
    font-weight: 400;
    line-height: 1.2;
    color: var(--text-dark);
    white-space: nowrap;
  }
  .card__figure {
    position: absolute;
    left: 95px;
    top: 110px;
    width: 236px;
    height: 359px;
    border-radius: 45% 55% 50% 50%;
    background: radial-gradient(ellipse at 60% 40%, rgba(19, 93, 140, 0.55), rgba(19, 93, 140, 0) 70%);
  }
  .card__details {
    position: absolute;
    right: 52px;
    top: 300px;
    text-align: right;
    color: var(--text-light);
  }
  .card__name {
    font-size: 38px;
    line-height: 1.2;
    margin-bottom: 46px;
  }
  .card__line {
    font-size: 29px;
    line-height: 1.2;
    margin-bottom: 38px;
  }
</style>
</head>
<body>
  <main class="card">
    <div class="card__band"></div>
    <div class="card__panel-wrap">
      <div class="card__panel">
        <h1 class="card__title">Physiotherapeutin</h1>
        <div class="card__figure" role="img" aria-label="Stylised figure of a leaping person in deep blue"></div>
      </div>
    </div>
    <div class="card__details">
      <p class="card__name">Name: Lilla Varga</p>
      <p class="card__line">Phone num: +43 664 5290 4816</p>
      <p class="card__line">e-mail: lilla.praxis@brelomail.com</p>
    </div>
  </main>
</body>
</html>
```